Web design for Crowdfunding site HaloFundry.com

We need a web design for christian crowdfunding website. Here is the challenge: We need responsive layout that is targeted first in iPad size of screen. It should also scale somehow down to iPhone size of screens. Web layout can be about the same size as iPad screen.

Screens should work so that main page scrolls not but only certain part of the screen scrolls and always one "page" at time. We can implement these "scrolls" then later with javascript but now we need only design. The challenge is to create this kind of hybrid website / app look.

Target is at first to raise funds to orphan people needing about $40 per month for their living and education. There is always some organization which takes care of these kids. Later there will be other christian missions included. At first we are looking to find monthly supporters.

You can be as creative as you want :) As you see from the look and feel sector, I am not looking any same traditional look which many "help kids" sites have. I am looking to reach now younger generation and therefore iPad and mobile are the main screen sizes.

Inspirational designs:
- https://brightpixelhub.example/profiles/studiokelvira/designs/418263?from=%2Fbrowse%2Fxhr%2Fdesigns%3Fcategory%3Dmobile-app-design
- http://www.artmarketloop.example/design/7261540 Clear, simple visuals
- http://www.artmarketloop.example/design/8420917 Header
- http://www.artmarketloop.example/design/6394275 Contrast in the colors, i think is powerfull

Some terms could be: Kids play, kids are learning (in the school). No static posture but living like kids are. I wonder also how we could also add little bit gaming style even though the question is of reali life of real people. Giving should be rewarding.

Target Market(s)

People who want help other people.

Industry/Entity Type

Christian

Number of Pages Required

4 page

Requirements
Must have
• Homepage. Mission page (In my wireframes it was one kid).
Nice to have
• Other pages and some idea how to scroll. 4 pages is no must. If you feel easy, please give first some draft and I give comments on that.

```html
<!DOCTYPE html>
<html lang="en">
<head>
<meta charset="utf-8">
<title>HaloFundry – Mission: Orphan Maria</title>
<link href="https://fonts.googleapis.com/css2?family=Montserrat:wght@400;500;600;700&family=Open+Sans:wght@400;600&display=swap" rel="stylesheet">
<style>
  :root{
    --ink:#111111;
    --text:#555555;
    --muted:#8a8a8a;
    --paper:#ffffff;
    --header:#f4f4f4;
    --footer:#efefef;
    --yellow:#fcb415;
    --red:#e8323a;
    --panel:#1c1c1c;
    --panel-row:#2a2a2a;
    --panel-line:#3a3a3a;
    --photo-a:#5b6166;
    --photo-b:#8c9297;
  }
  *{box-sizing:border-box;margin:0;padding:0}
  html,body{width:1200px;height:935px;overflow:hidden;background:var(--paper)}
  body{font-family:"Montserrat",sans-serif;color:var(--ink);position:relative}

  .site-header{position:absolute;left:0;top:0;width:1200px;height:82px;background:var(--header)}
  .missions-link{position:absolute;left:30px;top:27px;display:flex;align-items:center;gap:12px;font-size:21px;font-weight:500;color:var(--muted);letter-spacing:.3px;white-space:nowrap}
  .brand{position:absolute;left:0;width:1200px;top:20px;text-align:center;font-size:38px;font-weight:600;color:var(--ink);letter-spacing:.5px}
  .auth{position:absolute;right:22px;top:20px;display:flex;gap:14px}
  .auth a{display:block;height:34px;line-height:34px;padding:0 18px;font-size:16px;font-weight:600;color:#fff;text-decoration:none;white-space:nowrap;text-align:center}
  .btn-login{background:var(--ink);min-width:94px}
  .btn-signup{background:var(--red);min-width:106px}

  .story{position:absolute;left:0;top:82px;width:776px;height:853px;background:var(--paper)}
  .mission-title{position:absolute;left:32px;top:24px;display:flex;align-items:center;gap:30px}
  .mission-title h1{font-size:30px;font-weight:600;color:var(--ink);white-space:nowrap}
  .tabs{position:absolute;left:35px;top:102px;width:714px;height:54px;display:flex;gap:4px}
  .tab{flex:1;background:var(--yellow);color:var(--ink);font-size:20px;font-weight:500;text-align:center;line-height:54px;position:relative}
  .tab.active{background:var(--ink);color:var(--yellow)}
  .tab.active::after{content:"";position:absolute;left:50%;bottom:-12px;margin-left:-12px;border:12px solid transparent;border-bottom:0;border-top-color:var(--ink)}
  .story-lead{position:absolute;left:35px;top:174px;width:714px;font-size:30px;line-height:36px;font-weight:600;color:var(--text)}
  .story p{position:absolute;left:35px;width:714px;font-family:"Open Sans",sans-serif;font-size:15px;line-height:27px;color:var(--text)}
  .p1{top:254px}
  .p2{top:660px}
  .story-photo{position:absolute;left:35px;top:400px;width:714px;height:240px;background:linear-gradient(90deg,var(--photo-a),var(--photo-b) 50%,var(--photo-a))}
  .site-footer{position:absolute;left:0;bottom:0;width:434px;height:80px;background:var(--footer);font-size:16px;color:var(--text);padding:30px 0 0 50px;white-space:nowrap}
  .site-footer a{color:var(--red);text-decoration:none}

  .sidebar{position:absolute;left:776px;top:82px;width:424px;height:853px;background:var(--panel);color:#fff}
  .child-name{height:120px;padding:20px 30px 0 30px;position:relative}
  .child-name h2{font-size:29px;font-weight:600;color:var(--yellow);white-space:nowrap}
  .social{position:absolute;right:26px;top:28px;display:flex;gap:12px}
  .social span{width:16px;height:16px;background:#fff;display:block}
  .location{margin-top:24px;display:flex;align-items:center;gap:12px;font-size:24px;font-weight:600;color:var(--red)}
  .organization{height:51px;background:var(--panel-row);padding:0 30px;line-height:51px;font-size:22px;font-weight:500;color:#bdbdbd;white-space:nowrap}

  .support{height:292px;background:var(--yellow);position:relative}
  .support h3{position:absolute;left:28px;top:24px;font-size:32px;font-weight:500;color:#fff}
  .supporters{position:absolute;left:204px;top:22px;display:flex;gap:10px}
  .supporters span{width:34px;height:34px;border-radius:50%;border:3px solid #fff;background:rgba(255,255,255,.35)}
  .support .chevron{position:absolute;right:26px;top:30px}
  .support-now{position:absolute;left:28px;top:78px;font-size:16px;font-weight:500;color:var(--ink);white-space:nowrap}
  .progress{position:absolute;left:26px;top:128px}
  .given{position:absolute;left:174px;top:138px;font-size:32px;font-weight:700;color:#fff;white-space:nowrap}
  .needed{position:absolute;left:174px;top:184px;font-size:20px;color:#fff;white-space:nowrap}
  .per-month{position:absolute;left:174px;top:222px;display:flex;align-items:center;gap:10px;font-size:20px;font-weight:500;color:#fff;white-space:nowrap}

  .participate{height:69px;background:var(--red);padding-left:30px;line-height:69px;font-size:30px;font-weight:500;color:#fff}
  .options{list-style:none}
  .option{height:56px;border-bottom:1px solid var(--panel-line);display:flex;align-items:center;padding:0 20px 0 30px;font-size:20px;font-weight:500;color:#fff;white-space:nowrap}
  .check{width:28px;height:28px;border:2px solid #555;margin-right:26px;flex:none}
  .option .label{flex:1;white-space:nowrap}
  .option .label.short{flex:none}
  .amount-field{width:140px;height:34px;line-height:32px;background:var(--ink);border:1px solid #444;font-size:15px;text-align:center;margin:0 30px 0 auto;color:#fff;flex:none}
  .option svg{flex:none}
</style>
</head>
<body>
  <header class="site-header">
    <div class="missions-link">
      <svg width="34" height="22" viewBox="0 0 34 22"><g fill="#8a8a8a"><rect y="0" width="34" height="3"/><rect y="9" width="34" height="3"/><rect y="18" width="34" height="3"/></g></svg>
      SEE THE MISSIONS
    </div>
    <div class="brand">HALOFUNDRY</div>
    <nav class="auth">
      <a class="btn-login" href="#">LOGIN</a>
      <a class="btn-signup" href="#">SIGN UP</a>
    </nav>
  </header>

  <main class="story">
    <div class="mission-title">
      <svg width="56" height="58" viewBox="0 0 56 58" fill="none" stroke="#888" stroke-width="2.5">
        <path d="M6 26 L28 6 L50 26"/>
        <path d="M12 21 V40 M44 21 V40"/>
        <circle cx="20" cy="34" r="6"/><circle cx="36" cy="34" r="6"/>
        <path d="M8 56 Q8 44 20 44 Q32 44 32 56"/><path d="M26 56 Q26 44 38 44 Q50 44 50 56"/>
      </svg>
      <h1>Mission : Orphan Maria, 11y</h1>
    </div>
    <nav class="tabs">
      <div class="tab active">STORY</div>
      <div class="tab">UPDATES</div>
      <div class="tab">COMMENTS</div>
    </nav>
    <h2 class="story-lead">Neque porro quisquam est qui dolorem ipsum quia dolor sit amet,</h2>
    <p class="p1">Sed ut perspiciatis unde omnis iste natus error sit voluptatem accusantium doloremque laudantium, totam rem aperiam, eaque ipsa quae ab illo inventore veritatis et quasi architecto beatae vitae dicta sunt explicabo. Nemo enim ipsam voluptatem quia voluptas sit aspernatur aut odit aut fugit, sed quia consequuntur magni dolores eos qui ratione voluptatem sequi nesciunt.</p>
    <div class="story-photo" role="img" aria-label="Photo of Maria, a young girl hugging a teddy bear in front of a weathered wooden door"></div>
    <p class="p2">Sed ut perspiciatis unde omnis iste natus error sit voluptatem accusantium doloremque laudantium, totam rem aperiam, eaque ipsa quae ab illo inventore veritatis et quasi architecto beatae vitae dicta sunt explicabo.</p>
    <footer class="site-footer">© Copyright 2016, <a href="#">companyname.com</a></footer>
  </main>

  <aside class="sidebar">
    <section class="child-name">
      <h2>Name : Maria ,11y</h2>
      <div class="social"><span></span><span></span><span></span></div>
      <div class="location">
        <svg width="16" height="22" viewBox="0 0 16 22"><path d="M8 0 A8 8 0 0 1 16 8 C16 14 8 22 8 22 C8 22 0 14 0 8 A8 8 0 0 1 8 0 Z" fill="#e8323a"/><circle cx="8" cy="8" r="3" fill="#1c1c1c"/></svg>
        Kalkutta
      </div>
    </section>
    <div class="organization">Organization : Jacob</div>

    <section class="support">
      <h3>Support</h3>
      <div class="supporters"><span></span><span></span><span></span><span></span></div>
      <svg class="chevron" width="14" height="22" viewBox="0 0 14 22"><path d="M3 3 L11 11 L3 19" fill="none" stroke="#222" stroke-width="3"/></svg>
      <div class="support-now">My support is now : $5 / Month</div>
      <svg class="progress" width="124" height="124" viewBox="0 0 124 124">
        <circle cx="62" cy="62" r="52" fill="none" stroke="#fff" stroke-width="12"/>
        <circle cx="62" cy="62" r="52" fill="none" stroke="#e8323a" stroke-width="12" stroke-dasharray="147 327" transform="rotate(-90 62 62)"/>
        <text x="58" y="72" text-anchor="middle" font-family="Montserrat, sans-serif" font-size="30" font-weight="500" fill="#e8323a">45</text>
        <text x="80" y="56" font-family="Montserrat, sans-serif" font-size="12" fill="#e8323a">%</text>
      </svg>
      <div class="given">$15 given</div>
      <div class="needed">of total $35 needed</div>
      <div class="per-month">
        <svg width="22" height="22" viewBox="0 0 22 22" fill="none" stroke="#222" stroke-width="2"><rect x="2" y="4" width="18" height="16"/><path d="M2 9 H20 M7 1 V6 M15 1 V6 M6 13 H8 M10 13 H12 M14 13 H16 M6 16 H8 M10 16 H12"/></svg>
        Per month need
      </div>
    </section>

    <div class="participate">Participate</div>
    <ul class="options">
      <li class="option"><span class="check"></span><span class="label">I am in $1 / month</span><svg width="22" height="18" viewBox="0 0 22 18" fill="none" stroke="#666" stroke-width="2"><path d="M1 6 H21 L18 17 H4 Z M6 6 L9 1 M16 6 L13 1"/></svg></li>
      <li class="option"><span class="check"></span><span class="label">Increased, $5 / month</span><svg width="22" height="18" viewBox="0 0 22 18" fill="none" stroke="#666" stroke-width="2"><path d="M1 6 H21 L18 17 H4 Z M6 6 L9 1 M16 6 L13 1"/></svg></li>
      <li class="option"><span class="check"></span><span class="label">Decent help, $10 / month</span><svg width="22" height="18" viewBox="0 0 22 18" fill="none" stroke="#666" stroke-width="2"><path d="M1 6 H21 L18 17 H4 Z M6 6 L9 1 M16 6 L13 1"/></svg></li>
      <li class="option"><span class="check"></span><span class="label">Whole kid, $35 / month</span><svg width="22" height="18" viewBox="0 0 22 18" fill="none" stroke="#666" stroke-width="2"><path d="M1 6 H21 L18 17 H4 Z M6 6 L9 1 M16 6 L13 1"/></svg></li>
      <li class="option"><span class="check"></span><span class="label short">My Amount</span><span class="amount-field">Enter Amount</span><svg width="22" height="18" viewBox="0 0 22 18" fill="none" stroke="#666" stroke-width="2"><path d="M1 6 H21 L18 17 H4 Z M6 6 L9 1 M16 6 L13 1"/></svg></li>
    </ul>
  </aside>
</body>
</html>
```